Bright Arch Group business card

Bright Arch Group is the parent company of Bright Arch Building, Bright Arch Plumbing and Bright Arch Renovating. We require a sophisticated business card that covers all aspects of the building and plumbing space without using told or construction items.

Industry/Entity Type

Construction Company

Contact Information for Business Card

Gareth Pimley
Director
0472915083
gareth@brightarch.com.au
Www.brightarch.com.au

Font styles to use
Serif
Sans Serif

Colors
3176b5
ffce3e
0692cd
34a7d8
fbee3e
faa54b

Requirements
Must have
• Logo on front
• Logo and details on rear.
Nice to have
• Maybe water mark or shadow effect with logo
Should not have
• Tools or any construction associated items

```html
<!DOCTYPE html>
<html lang="en">
<head>
<meta charset="utf-8">
<title>Bright Arch Group – Business Card</title>
<link href="https://fonts.googleapis.com/css2?family=Arimo:wght@400&family=Jost:wght@400&display=swap" rel="stylesheet">
<style>
  :root {
    --paper: #ffffff;
    --ink: #1f1f1f;
    --frame: #000000;
    --card-blue: #1c78b8;
    --accent-orange: #f7941d;
    --name-ink: #262626;
  }
  * { margin: 0; padding: 0; box-sizing: border-box; }
  html, body {
    width: 1050px;
    height: 1200px;
    overflow: hidden;
    background: var(--paper);
  }
  .sheet {
    position: relative;
    width: 1050px;
    height: 1200px;
  }

  /* Front side */
  .card-front {
    position: absolute;
    left: 133px;
    top: 126px;
    width: 786px;
    height: 449px;
    border: 3px solid var(--frame);
    background: var(--paper);
    display: flex;
    align-items: center;
    justify-content: center;
    gap: 22px;
  }
  .brand-dot {
    border-radius: 50%;
    background: var(--accent-orange);
    flex: none;
  }
  .card-front .brand-dot { width: 46px; height: 46px; }
  .brand-name {
    font-family: "Jost", sans-serif;
    font-weight: 400;
    text-transform: uppercase;
    white-space: nowrap;
  }
  .card-front .brand-name {
    font-size: 54px;
    letter-spacing: 10px;
    color: var(--ink);
  }

  /* Back side */
  .card-back {
    position: absolute;
    left: 130px;
    top: 626px;
    width: 789px;
    height: 451px;
    background: var(--card-blue);
    font-family: "Arimo", sans-serif;
  }
  .back-brand {
    position: absolute;
    left: 30px;
    top: 42px;
    display: flex;
    align-items: center;
    gap: 10px;
  }
  .back-brand .brand-dot { width: 20px; height: 20px; }
  .back-brand .brand-name {
    font-size: 22px;
    letter-spacing: 4px;
    color: var(--ink);
  }
  .holder {
    position: absolute;
    right: 17px;
    top: 98px;
    text-align: right;
    color: var(--name-ink);
  }
  .holder-name {
    font-size: 42px;
    line-height: 1;
  }
  .holder-role {
    font-size: 22px;
    line-height: 1;
    margin-top: 8px;
  }
  .divider {
    position: absolute;
    left: 0;
    top: 178px;
    width: 100%;
    height: 3px;
    background: var(--accent-orange);
  }
  .contact-list {
    position: absolute;
    left: 30px;
    top: 240px;
    list-style: none;
  }
  .contact-item {
    display: flex;
    align-items: center;
    gap: 14px;
    height: 38px;
    margin-bottom: 18px;
    color: var(--accent-orange);
    font-size: 30px;
    line-height: 1;
  }
  .contact-icon {
    width: 37px;
    height: 37px;
    flex: none;
  }
</style>
</head>
<body>
<main class="sheet">

  <section class="card-front" aria-label="Card front">
    <span class="brand-dot"></span>
    <span class="brand-name">Bright Arch Group</span>
  </section>

  <section class="card-back" aria-label="Card back">
    <div class="back-brand">
      <span class="brand-dot"></span>
      <span class="brand-name">Bright Arch Group</span>
    </div>

    <div class="holder">
      <p class="holder-name">Gareth Pimley</p>
      <p class="holder-role">Director</p>
    </div>

    <div class="divider"></div>

    <ul class="contact-list">
      <li class="contact-item">
        <svg class="contact-icon" viewBox="0 0 40 40" aria-hidden="true">
          <circle cx="20" cy="20" r="17.5" fill="none" stroke="#f7941d" stroke-width="3"/>
          <path d="M13 11c1-1 2.5-1 3.2 0l2 3c.6 1 .3 2-.5 2.6l-1.2 1c.9 2.4 2.7 4.3 5 5.3l1-1.2c.7-.8 1.7-1 2.6-.4l3 2c1 .7 1 2.2 0 3.1l-1.6 1.5c-1.2 1.1-3 1.3-4.5.6C17 26.5 13.5 23 11.4 17.8c-.6-1.5-.3-3.2.8-4.4z" fill="none" stroke="#f7941d" stroke-width="2.2" stroke-linejoin="round"/>
        </svg>
        <span>04 7291 5083</span>
      </li>
      <li class="contact-item">
        <svg class="contact-icon" viewBox="0 0 40 40" aria-hidden="true">
          <circle cx="20" cy="20" r="17.5" fill="none" stroke="#f7941d" stroke-width="3"/>
          <circle cx="20" cy="20" r="10" fill="#f7941d"/>
          <path d="M15 14c2 0 3 1.5 2.5 3s-2.5 1.5-2 3.5 2 2 1.5 4M24 13c-1 2 0 3 1.5 3.5s1.5 2.5 0 3.5-1 3 .5 4" fill="none" stroke="#1c78b8" stroke-width="1.6" stroke-linecap="round"/>
        </svg>
        <span>www.brightarch.com.au</span>
      </li>
      <li class="contact-item">
        <svg class="contact-icon" viewBox="0 0 40 40" aria-hidden="true">
          <circle cx="20" cy="20" r="17.5" fill="none" stroke="#f7941d" stroke-width="3"/>
          <rect x="10.5" y="13.5" width="19" height="13" fill="none" stroke="#f7941d" stroke-width="2"/>
          <path d="M10.5 13.5 20 21l9.5-7.5M10.5 26.5l7-6M29.5 26.5l-7-6" fill="none" stroke="#f7941d" stroke-width="1.6"/>
        </svg>
        <span>gareth@brightarch.com.au</span>
      </li>
    </ul>
  </section>

</main>
</body>
</html>
```